Sale Hang Tag

Design a bright, cheerful, compelling, call to action sale tag for a lighting showroom. The tag will be used to move older or discontinued product at a really good price. Upscale, friendly, neighbor store. Size should be no larger than 4 by 6 inches.

Call

```html
<!DOCTYPE html>
<html lang="en">
<head>
<meta charset="utf-8">
<title>Sale Hang Tag – Buy Me</title>
<link rel="stylesheet" href="https://fonts.googleapis.com/css2?family=Great+Vibes&family=Didact+Gothic&display=swap">
<style>
  :root {
    --page: #ece6de;
    --tag-teal: #40736f;
    --tag-white: #ffffff;
    --eyelet-orange: #f2421c;
    --eyelet-hole: #2c2a28;
  }

  html, body {
    margin: 0;
    width: 1200px;
    height: 750px;
    overflow: hidden;
    background: var(--page);
  }

  .canvas {
    position: relative;
    width: 1200px;
    height: 750px;
  }

  .hang-tag {
    position: absolute;
    left: 434px;
    top: 111px;
    width: 332px;
    height: 528px;
    transform: scale(1.25);
    transform-origin: center center;
    font-family: "Didact Gothic", sans-serif;
    color: var(--tag-white);
  }

  .tag-shape {
    position: absolute;
    inset: 0;
    background: var(--tag-teal);
    clip-path: polygon(32px 0, 300px 0, 332px 28px, 332px 528px, 0 528px, 0 28px);
    box-shadow: 0 6px 18px rgba(0, 0, 0, 0.25);
  }

  .eyelet {
    position: absolute;
    left: 126px;
    top: 0;
    width: 80px;
    height: 92px;
  }

  .headline {
    position: absolute;
    left: 0;
    top: 0;
    margin: 0;
    font-family: "Great Vibes", cursive;
    font-weight: 400;
    line-height: 1;
  }

  .headline-buy {
    position: absolute;
    left: 34px;
    top: 98px;
    font-size: 104px;
  }

  .headline-me {
    position: absolute;
    left: 150px;
    top: 176px;
    font-size: 104px;
  }

  .price-box {
    position: absolute;
    left: 10px;
    top: 278px;
    width: 310px;
    height: 138px;
    background: var(--tag-white);
    border-radius: 18px;
  }

  .price-label {
    position: absolute;
    left: 10px;
    top: 7px;
    font-size: 16px;
    letter-spacing: 0.5px;
    color: var(--tag-teal);
  }

  .divider {
    position: absolute;
    left: 10px;
    top: 426px;
    width: 310px;
    height: 4px;
    background: var(--tag-white);
  }

  .size-field {
    position: absolute;
    left: 68px;
    top: 438px;
    display: flex;
    height: 27px;
    font-size: 21px;
    line-height: 25px;
  }

  .size-label {
    width: 94px;
    background: var(--tag-white);
    color: var(--tag-teal);
    text-align: center;
    border: 1px solid var(--tag-white);
  }

  .size-value {
    width: 98px;
    color: var(--tag-white);
    text-align: center;
    border: 1px solid var(--tag-white);
  }

  .social-handle {
    position: absolute;
    right: 12px;
    top: 484px;
    display: flex;
    align-items: center;
    gap: 7px;
    font-size: 18px;
  }

  .social-dot {
    width: 14px;
    height: 14px;
    border: 2px solid var(--tag-white);
    border-radius: 50%;
  }
</style>
</head>
<body>
  <main class="canvas">
    <article class="hang-tag">
      <div class="tag-shape"></div>

      <svg class="eyelet" viewBox="0 0 80 92" aria-hidden="true">
        <path d="M14 0 H66 V16 A40 40 0 1 1 14 16 Z" fill="var(--eyelet-orange)"/>
        <circle cx="40" cy="46" r="12" fill="var(--eyelet-hole)"/>
      </svg>

      <h1 class="headline">
        <span class="headline-buy">Buy</span>
        <span class="headline-me">Me</span>
      </h1>

      <div class="price-box">
        <span class="price-label">PRICE</span>
      </div>

      <div class="divider"></div>

      <div class="size-field">
        <span class="size-label">Size</span>
        <span class="size-value">Medium</span>
      </div>

      <div class="social-handle">
        <span class="social-dot"></span>
        <span>@lumenlane</span>
      </div>
    </article>
  </main>
</body>
</html>
```